Need a book cover!

Attached is a design for a book cover. Need it to be better. Same text just better design. Use headshot image along side the author bio on the back cover.

```html
<!DOCTYPE html>
<html lang="en">
<head>
<meta charset="utf-8">
<title>Busted — Book Cover</title>
<link rel="stylesheet" href="https://fonts.googleapis.com/css2?family=Montserrat:ital,wght@1,700&family=Questrial&family=Russo+One&family=Tinos:ital,wght@0,400;1,700&display=swap">
<style>
  :root {
    --tan: #cd8f65;
    --brown: #66412a;
    --spine: #000000;
    --ink-light: #ffffff;
    --red: #d1232e;
    --photo-top: #4a3a2c;
    --photo-mid: #2f2620;
    --photo-low: #1d1713;
    --byline: #8f8d88;
    --author-photo-a: #3f6b3a;
    --author-photo-b: #8a8a86;
  }
  * { margin: 0; padding: 0; box-sizing: border-box; }
  html, body { width: 1200px; height: 776px; overflow: hidden; background: #fff; }
  .cover { position: relative; width: 1200px; height: 776px; overflow: hidden; }

  /* Back cover */
  .back { position: absolute; left: 0; top: 0; width: 557px; height: 776px; background: var(--brown); color: var(--ink-light); }
  .back-blurb { position: absolute; left: 0; top: 0; width: 557px; height: 419px; background: var(--tan); }
  .tagline, .about-heading {
    position: absolute; left: 0; width: 590px; text-align: center;
    font-family: "Montserrat", sans-serif; font-style: italic; font-weight: 700; font-size: 21px;
  }
  .tagline { top: 48px; }
  .about-heading { top: 436px; width: 582px; }
  .copy {
    font-family: "Questrial", sans-serif; font-size: 13.2px; line-height: 16.5px; text-align: justify;
  }
  .intro { position: absolute; left: 48px; top: 94px; width: 503px; }
  .learn-list { position: absolute; left: 48px; top: 215px; width: 503px; list-style: none; }
  .learn-list li { position: relative; padding-left: 18px; text-align: left; }
  .learn-list li::before { content: "•"; position: absolute; left: 0; }
  .closing { position: absolute; left: 48px; top: 333px; width: 503px; }
  .closing em { font-family: "Montserrat", sans-serif; font-weight: 700; font-size: 14px; }
  .bio { position: absolute; left: 105px; top: 494px; width: 212px; }
  .author-photo {
    position: absolute; left: 362px; top: 497px; width: 135px; height: 134px;
    background: linear-gradient(135deg, var(--author-photo-a) 0%, var(--author-photo-b) 100%);
  }

  /* Spine */
  .spine { position: absolute; left: 557px; top: 0; width: 57px; height: 776px; background: var(--spine); color: var(--ink-light); }
  .spine-title, .spine-author {
    position: absolute; left: 29px; transform-origin: 0 0; transform: rotate(90deg);
    font-family: "Tinos", serif; font-size: 14.5px; white-space: nowrap;
    margin-left: 9px;
  }
  .spine-title { top: 104px; }
  .spine-author { top: 557px; letter-spacing: 0.5px; }

  /* Front cover */
  .front { position: absolute; left: 614px; top: 0; width: 586px; height: 776px; }
  .front-photo {
    position: absolute; inset: 0;
    background: radial-gradient(ellipse at 50% 40%, var(--photo-top) 0%, var(--photo-mid) 55%, var(--photo-low) 100%);
  }
  .title-art { position: absolute; left: 44px; top: 338px; width: 496px; height: 88px; }
  .subtitle {
    position: absolute; left: 50px; top: 450px; width: 490px; text-align: center;
    font-family: "Russo One", sans-serif; font-size: 20.5px; line-height: 26px; color: var(--ink-light);
    letter-spacing: 0.6px;
  }
  .byline {
    position: absolute; left: 200px; top: 727px; width: 200px; text-align: center;
    font-family: "Tinos", serif; font-style: italic; font-weight: 700; font-size: 12px; color: var(--byline);
  }
</style>
</head>
<body>
<div class="cover">
  <section class="back">
    <div class="back-blurb">
      <h2 class="tagline">Don’t Let the System Steamroll You.</h2>
      <p class="copy intro">Being charged with a crime is terrifying. One wrong move—or one wrong word—can wreck your future. But it doesn’t have to. In Busted, veteran defense attorney Marco-Luis Verrano walks you through every step of the criminal justice process, from arrest to arraignment, plea deal to trial, and beyond. Whether you’re facing your first misdemeanor or a serious felony, this book gives you the knowledge and tools you need to fight back smart. You’ll learn:</p>
      <ul class="copy learn-list">
        <li>What not to say to police (and why silence is your best friend).</li>
        <li>The real role of prosecutors—and why they’re not looking out for you.</li>
        <li>How bail, plea deals, and court hearings actually work.</li>
        <li>The biggest mistakes people make when they’re under investigation.</li>
        <li>How a good lawyer can challenge the evidence—and change the outcome.</li>
      </ul>
      <p class="copy closing"><em>Busted</em> is packed with clear, practical advice to help you protect your rights, avoid common traps, and take control of your defense. Whether you’ve been arrested, are under investigation, or just want to understand how the system works, this book is your first—and most important—line of defense.</p>
    </div>
    <h2 class="about-heading">About The Author</h2>
    <p class="copy bio">Marco-Luis Verrano is the managing attorney of Harborline Legal Group and a seasoned California criminal defense lawyer. Known for out-preparing prosecutors and standing up for the underdog, he’s helped thousands of clients protect their freedom, records, and futures.</p>
    <div class="author-photo" role="img" aria-label="Author headshot: smiling man in grey suit in front of green plants"></div>
  </section>

  <section class="spine">
    <div class="spine-title">Busted: How to Fight Back When You’re Facing Criminal Charges</div>
    <div class="spine-author">VERRANO</div>
  </section>

  <section class="front">
    <div class="front-photo" role="img" aria-label="Photograph: a serious man in a dark suit standing at a courtroom desk, two women in suits behind him"></div>
    <svg class="title-art" viewBox="0 0 496 88" aria-label="Busted">
      <text x="0" y="84" textLength="496" lengthAdjust="spacingAndGlyphs" fill="var(--red)" font-family="Russo One, sans-serif" font-size="112">BUSTED</text>
    </svg>
    <p class="subtitle">HOW TO FIGHT BACK WHEN YOU'RE<br>FACING CRIMINAL CHARGES</p>
    <p class="byline">BY MARCO-LUIS VERRANO</p>
  </section>
</div>
</body>
</html>
```